Modellprojekt in der Jugendhilfe sucht für Abschlussbroschüre ansprechendes Design
Zielgruppe
Wir sind ein Jugendhilfeträger und haben kürzlich ein dreijähriges Modellprojekt 'Qualitätsmarke-Gemeinsame Familienbegleitung' (Signet 'QM_Anerkennung' liegt anbei) beendet. Zielgruppen sind zum Einen Kinder und Jugendliche, die in Erziehungshilfe-Wohngruppen leben und zum Anderen Fach- und Führungskräfte in der Kinder- und Jugendhilfe. Über Ablauf und Schlussfolgerungen aus dem abgeschlossenen Modellprojekt soll eine 30-seitige Broschüre mit dem Titel 'Hier wächst Mitsprache' Untertitel 'Ein Wegweiser zur Qualitätsmarke' Auskunft geben.
Aufgabenstellung
- Broschüre im DIN A4 - Format,
- Dummy-Text für Projektstruktur und -beteiligte,
- Formschönes und dynamisches Design,
- Platzhalter für eigene Bilder (max. 3 pro Seite),
- die 6 Einrichtungslogos in einer Reihe auf dem Deckblatt vorne (unten),
- Der Broschüreninhalt ist in der PDF 'Kurzvorstellung enthalten',
- Vorgaben zum CD im PDF 'Hauptmanual KWF',
- Das KWF-Signet, wie im Manual beschrieben,
- das ebenfalls hochgeladene Gütesiegel kommt auf das Deckblatt

```html
<!DOCTYPE html>
<html lang="de">
<head>
<meta charset="utf-8">
<title>Hier wächst Mitsprache – Broschüre</title>
<link rel="stylesheet" href="https://fonts.googleapis.com/css2?family=Fira+Sans+Condensed:wght@400;600&family=IBM+Plex+Mono:wght@400;600&display=swap">
<style>
  :root{
    --bg:#efefef;
    --paper:#ffffff;
    --blue:#1d6fb8;
    --green:#2f6b45;
    --green-dark:#21503a;
    --chalk:#3c7a52;
    --orange:#e8571c;
    --lilac:#dfe2f2;
    --text:#3a3a3a;
    --grey:#8a8a8a;
    --head:"Fira Sans Condensed", sans-serif;
    --body:"IBM Plex Mono", monospace;
  }
  *{box-sizing:border-box;margin:0;padding:0}
  html,body{width:1200px;height:848px;overflow:hidden;background:var(--bg)}
  .canvas{position:relative;width:1200px;height:848px}
  .page{position:absolute;background:var(--paper);overflow:hidden}
  .abs{position:absolute}
  .placeholder{position:absolute}

  /* Cover */
  .cover{left:14px;top:151px;width:386px;height:546px}
  .cover-title{left:54px;top:350px;font-family:var(--head);font-weight:600;font-size:23px;line-height:28px;color:var(--blue)}
  .seal{left:22px;top:240px}
  .logos{left:54px;top:456px;width:310px;height:60px;font-family:var(--head);font-weight:400;color:var(--blue)}
  .logo{position:absolute;display:flex;align-items:flex-start;gap:4px;font-size:5px;line-height:6px}
  .logo .mark{width:6px;height:6px;background:var(--orange);flex:none}
  .logo-main{left:0;top:0;font-size:7px;line-height:8px;gap:5px}
  .logo-main .mark{width:26px;height:26px;background:var(--blue)}
  .logo-main .name{font-size:12px;line-height:13px}

  /* Spread */
  .spread{left:414px;top:151px;width:772px;height:546px;background:var(--paper)}
  .spread::after{content:"";position:absolute;left:386px;top:0;width:1px;height:100%;background:#e6e6e6}
  .story-title{left:36px;top:84px;font-family:var(--head);font-size:23px;color:var(--blue)}
  .story-sub{left:36px;top:113px;font-family:var(--head);font-size:8.6px;line-height:11.5px;color:var(--blue)}
  .col{position:absolute;font-family:var(--body);font-size:5px;line-height:8.2px;color:var(--text)}
  .col p{margin-bottom:8px}
  .col h3{font-family:var(--head);font-weight:400;font-size:7.3px;line-height:8.5px;color:var(--blue);margin-bottom:6px}
  .info-box{left:190px;top:294px;width:137px;height:206px;background:var(--lilac);border-radius:6px;padding:24px 8px 8px 10px}
  .info-box ul{list-style:none;font-family:var(--body);font-weight:600;font-size:4.8px;line-height:8.2px;color:#2c2c2c}
  .info-box li{position:relative;margin-bottom:8px;padding-left:6px}
  .info-box li::before{content:"›";position:absolute;left:-2px;top:-1px;font-size:8px;color:var(--blue)}
  .sidebar{left:592px;top:188px;width:139px;height:316px;background:var(--lilac);border-radius:6px;padding:40px 8px 8px 8px}
  .footer{position:absolute;top:521px;font-family:var(--body);font-size:4.2px;color:var(--grey)}
  .footer b{color:var(--blue);font-weight:600;margin-left:6px}
</style>
</head>
<body>
<div class="canvas">

  <!-- Cover -->
  <section class="page cover">
    <svg class="abs" width="386" height="330" viewBox="0 0 386 330">
      <defs>
        <linearGradient id="coverBoard" x1="0" y1="0" x2="1" y2="1">
          <stop offset="0" stop-color="#3b7b52"/>
          <stop offset="1" stop-color="#285c3d"/>
        </linearGradient>
      </defs>
      <path role="img" aria-label="Kreidetafel mit Pfeilen in alle Richtungen, Fragezeichen in der Mitte und einer Hand mit Kreide" d="M0 0H386V238Q200 262 0 306Z" fill="url(#coverBoard)"/>
      <path d="M0 306Q200 262 386 238" fill="none" stroke="var(--orange)" stroke-width="4"/>
    </svg>
    <svg class="abs seal" width="92" height="92" viewBox="0 0 92 92">
      <circle cx="46" cy="46" r="44" fill="#fff" stroke="#2b2b2b" stroke-width="1.2"/>
      <circle cx="46" cy="46" r="30" fill="var(--green-dark)" stroke="var(--chalk)" stroke-width="3"/>
    </svg>
    <h1 class="abs cover-title">Hier wächst Mitsprache –<br>Ein Wegweiser zur Qualitätsmarke</h1>
    <div class="abs logos">
      <div class="logo logo-main"><span class="mark"></span><span><span class="name">KWF</span><br>Verbund Küstenwerk<br>Familienhilfe</span></div>
      <div class="logo" style="left:100px;top:2px"><span class="mark"></span><span>Ev. Arbeitskreis<br>Förde</span></div>
      <div class="logo" style="left:170px;top:2px"><span class="mark"></span><span>Jugendwerk<br>Eiderland</span></div>
      <div class="logo" style="left:240px;top:2px"><span class="mark"></span><span>Kinderhilfe<br>Schleiufer</span></div>
      <div class="logo" style="left:100px;top:34px"><span class="mark"></span><span>Kinderhäuser<br>Seewinkel</span></div>
      <div class="logo" style="left:170px;top:34px"><span class="mark"></span><span>Pädagogische Hilfen<br>Heideland</span></div>
      <div class="logo" style="left:240px;top:34px"><span class="mark"></span><span>Sozialpäd. Hilfen<br>Marschland</span></div>
    </div>
  </section>

  <!-- Inner spread -->
  <section class="page spread">
    <svg class="abs" style="left:386px;top:0" width="386" height="240" viewBox="0 0 386 240">
      <defs>
        <linearGradient id="spreadBoard" x1="0" y1="0" x2="1" y2="1">
          <stop offset="0" stop-color="#2f6c45"/>
          <stop offset="1" stop-color="#3d7e55"/>
        </linearGradient>
      </defs>
      <path role="img" aria-label="Kreidetafel mit gelben Pfeilen und steigender Kurve, Hand mit gelber Kreide" d="M0 0H386V168Q200 200 0 226Z" fill="url(#spreadBoard)"/>
      <path d="M0 228Q200 202 386 170" fill="none" stroke="var(--orange)" stroke-width="3"/>
    </svg>

    <h2 class="abs story-title">Erfolgsstory</h2>
    <p class="abs story-sub">Blindtext steht hier Best Practise – Vorstellung vor Ort,<br>z.B. Selbstportrait/Rollenbeschreibung eines Gruppensprechers</p>

    <div class="placeholder" role="img" aria-label="Foto: Gruppe junger Leute sitzt lachend in einer Zugtür" style="left:302px;top:14px;width:198px;height:135px;background:linear-gradient(135deg,#c9473f,#b8a37a);border:4px solid #fff;transform:rotate(-5deg)"></div>

    <div class="col" style="left:36px;top:168px;width:142px">
      <h3>Ut enim ad minim veniam, quis nostrud</h3>
      <p>Nam libero tempore cum soluta nobis eligendi optio cumque nihil impedit quo minus id quod maxime placeat facere possimus omnis voluptas.</p>
    </div>
    <div class="placeholder" role="img" aria-label="Foto: zwei lachende Jugendliche sitzen nebeneinander" style="left:40px;top:236px;width:136px;height:112px;background:linear-gradient(135deg,#c8c0b2,#6f7d92);border:4px solid #fff;transform:rotate(6deg)"></div>
    <div class="col" style="left:36px;top:364px;width:142px">
      <p>Temporibus autem quibusdam et aut officiis debitis aut rerum necessitatibus saepe eveniet ut et voluptates repudiandae sint et molestiae non recusandae itaque earum rerum hic tenetur a sapiente delectus ut aut reiciendis voluptatibus maiores alias consequatur.</p>
      <p>Sed ut perspiciatis unde omnis iste natus error sit voluptatem accusantium doloremque.</p>
    </div>

    <div class="col" style="left:190px;top:168px;width:140px">
      <p>Inieni dolut aut a enist omnimi, te comnien tureius et acestio et, od mil minus idusantion nobita doluptis endenitatur se iustium, quia dellaut magnam et exceratur, consequamus quae dolendi rae sorib orum volore essima.</p>
    </div>

    <div class="abs info-box">
      <ul>
        <li>Fugiae coribus acestium facernate voluptat adelectae eaque seque dolo quibus.</li>
        <li>Neque omniene cullia is et reste et, volorum qui aliqui nihil min nimus mosam ditionse nobit que.</li>
        <li>Volorescil et ad quis eatatibus exceris repudis quiduci etureperest volupti culpa.</li>
        <li>Ommoloreptur aliquas et re et optaquisto eventur magnis eate dolupti andiaerum.</li>
      </ul>
    </div>
    <div class="placeholder" role="img" aria-label="Illustration: gelber Kofferanhänger mit Aufschrift Good to know" style="left:254px;top:270px;width:92px;height:42px;background:#f3b92a;border-radius:6px;transform:rotate(-14deg)"></div>

    <div class="col" style="left:586px;top:268px;width:0"></div>
    <div class="col" style="left:441px;top:268px;width:144px">
      <p>Dolenti urendam iur aut voluptate nis ape voluptis doluptiorem et ad quistio earunt, ipsaepe rferiostio rianihit autem eatur, nonsequias denesci umquist otatiur quide conse volorerh endebit.</p>
      <h3>At atquatum eaque doluptatis es maximag nienis et</h3>
      <p>Eosam, assunt et volupta nem quibus ipsam dus est quis reribus et eiuntores natet lam autempe rorit, que vendaes acit officate vit, aut iunt fugit alignia nem que eum liqui autem.</p>
      <h3>Millab ipitatis mo quis aut porepudam, ventis ea aliquissi occus.</h3>
      <p>At audis magnam et as dem et ut int porerunt aspiciam ent pres est laborro officit.</p>
    </div>

    <div class="abs sidebar">
      <div class="col" style="position:static">
        <h3>Acestio et, od mil minus</h3>
        <p>Idusantion nobita doluptis endenitatur se iustium, quia dellaut magnam et exceratur, consequamus quae dolendi rae. Solupta dolo que pori nimini sima eum et ullam seque nam volorrum.</p>
        <p>Quis dent vellaborem endi in pe nos ipsanit offic toreici ut ut as idemqua sperum hsequaes doluptatem sin pore volorume pera nonseque molorem.</p>
        <p>Unt peratem ent estende min explab idis archiciendis qui volum velecabo ebis doles doloreptam ipistrunt oditas malos nulpa aut lacepernam.</p>
        <p>Simet eos moditate volupta ectaspi catius ex eum explibus.</p>
      </div>
    </div>
    <svg class="abs" style="left:683px;top:155px" width="70" height="70" viewBox="0 0 70 70">
      <circle role="img" aria-label="Portraitfoto einer lächelnden Gruppensprecherin" cx="34" cy="34" r="32" fill="#c48a6a" stroke="#3d9a3f" stroke-width="3"/>
    </svg>
    <svg class="abs" style="left:656px;top:176px" width="18" height="24" viewBox="0 0 18 24">
      <line x1="9" y1="12" x2="9" y2="23" stroke="#777" stroke-width="1.2"/>
      <circle cx="9" cy="8" r="7" fill="var(--orange)"/>
    </svg>

    <div class="footer" style="left:36px">Hier wächst Mitsprache · Ein Wegweiser zur Qualitätsmarke</div>
    <div class="footer" style="right:36px">Hier wächst Mitsprache · Ein Wegweiser zur Qualitätsmarke<b>| 3</b></div>
  </section>

</div>
</body>
</html>
```